Copper lark buildworks

Copper lark buildworks is a small construction company.
Who is a licenced builder, Carpenter, joiner,
working on heritage ,new build, speacial projects and sometimes furniture

Industry/Entity Type

Construction

```html
<!DOCTYPE html>
<html lang="en">
<head>
<meta charset="utf-8">
<title>Copper lark buildworks – Business Card</title>
<link rel="stylesheet" href="https://fonts.googleapis.com/css2?family=Questrial&family=Open+Sans:wght@800&family=Abel&display=swap">
<style>
  :root {
    --page-bg: #e9e7e2;
    --card-green: #1e6234;
    --card-green-deep: #17532b;
    --accent-green: #8bc653;
    --band-white: #ffffff;
    --text-white: #ffffff;
    --text-green: #1e6234;
  }
  * { margin: 0; padding: 0; box-sizing: border-box; }
  html, body {
    width: 1200px; height: 788px; overflow: hidden;
    background: var(--page-bg);
  }
  .stage {
    width: 1200px; height: 788px;
    display: flex; align-items: center; justify-content: center;
  }
  .business-card {
    position: relative;
    width: 860px; height: 492px;
    background: linear-gradient(135deg, var(--card-green) 0%, var(--card-green-deep) 100%);
    border-radius: 6px;
    box-shadow: 0 10px 30px rgba(0,0,0,0.25);
    overflow: hidden;
  }
  .name-band {
    position: absolute;
    left: 0; top: 62px;
    width: 430px; height: 74px;
    background: var(--band-white);
    display: flex; align-items: center;
    padding-left: 48px;
    font-size: 46px;
    color: var(--text-green);
    white-space: nowrap;
  }
  .name-first {
    font-family: "Questrial", sans-serif;
    margin-right: 14px;
  }
  .name-last {
    font-family: "Open Sans", sans-serif;
    font-weight: 800;
  }
  .job-title {
    position: absolute;
    left: 196px; top: 146px;
    font-family: "Open Sans", sans-serif;
    font-weight: 800;
    font-size: 22px;
    letter-spacing: 0.5px;
    color: var(--text-white);
  }
  .contact-list {
    position: absolute;
    left: 48px; top: 212px;
    list-style: none;
  }
  .contact-item {
    display: flex; align-items: center;
    height: 56px;
    font-family: "Questrial", sans-serif;
    font-size: 27px;
    letter-spacing: 0.5px;
    color: var(--text-white);
  }
  .contact-icon {
    width: 38px; height: 38px;
    margin-right: 22px;
    flex: none;
  }
  .brand-block {
    position: absolute;
    left: 500px; top: 60px;
    width: 320px;
    display: flex; flex-direction: column; align-items: center;
  }
  .brand-mark {
    width: 220px; height: 220px;
    border-radius: 50%;
    background: var(--accent-green);
  }
  .brand-name {
    margin-top: 34px;
    font-family: "Abel", sans-serif;
    font-size: 40px;
    line-height: 1.1;
    text-align: center;
    color: var(--text-white);
  }
</style>
</head>
<body>
<main class="stage">
  <article class="business-card">
    <div class="name-band">
      <span class="name-first">Marcus</span><span class="name-last">Hale</span>
    </div>
    <p class="job-title">Representative</p>

    <ul class="contact-list">
      <li class="contact-item">
        <svg class="contact-icon" viewBox="0 0 38 38" aria-hidden="true">
          <circle cx="19" cy="19" r="19" fill="var(--accent-green)"/>
          <rect x="9" y="12" width="20" height="14" fill="none" stroke="var(--card-green)" stroke-width="2.4"/>
          <polyline points="9,12 19,21 29,12" fill="none" stroke="var(--card-green)" stroke-width="2.4"/>
        </svg>
        info@copperlark.com
      </li>
      <li class="contact-item">
        <svg class="contact-icon" viewBox="0 0 38 38" aria-hidden="true">
          <circle cx="19" cy="19" r="19" fill="var(--accent-green)"/>
          <path d="M13 10 l5 5 -3 3 c1.5 3 3.5 5 6 6 l3 -3 5 5 -3 3 c-8 0 -16 -8 -16 -16 z" fill="var(--card-green)"/>
        </svg>
        +042 730 2264
      </li>
      <li class="contact-item">
        <svg class="contact-icon" viewBox="0 0 38 38" aria-hidden="true">
          <circle cx="19" cy="19" r="19" fill="var(--accent-green)"/>
          <polygon points="19,9 29,18 26,18 26,28 12,28 12,18 9,18" fill="var(--card-green)"/>
          <rect x="17" y="21" width="4" height="7" fill="var(--accent-green)"/>
        </svg>
        copperlark.com
      </li>
      <li class="contact-item">
        <svg class="contact-icon" viewBox="0 0 38 38" aria-hidden="true">
          <circle cx="19" cy="19" r="19" fill="var(--accent-green)"/>
          <circle cx="19" cy="19" r="10" fill="none" stroke="var(--card-green)" stroke-width="2.4"/>
          <ellipse cx="19" cy="19" rx="4.5" ry="10" fill="none" stroke="var(--card-green)" stroke-width="2"/>
          <line x1="9" y1="19" x2="29" y2="19" stroke="var(--card-green)" stroke-width="2"/>
        </svg>
        copperlark.com
      </li>
    </ul>

    <div class="brand-block">
      <div class="brand-mark" aria-hidden="true"></div>
      <p class="brand-name">Copper lark buildworks</p>
    </div>
  </article>
</main>
</body>
</html>
```